Business Card and Letterhead Design Project

I am starting my own building design business in Melbourne. The business will use my experience to help people make balanced life choices for building and renovating. My target audience is women -particularly mothers. I aim to be approachable and economical. I would like to see a design that uses greens or blues - natural colours. A lot of my work balances design and construction management so design should be flexible.

I want a double sided business card design and a letterhead design that I can use on all office correspondance

Design should have a clean crisp feel - a bit edgey in a feminine way.

Target Market(s)

Potential clients.

Industry/Entity Type

Construction

Requirements
Must have
• Harbourline Design Studio
Rosalind Tebbutt B.Arch

0498 273 461
rosalind@harbourlinedesignstudio.com.au

14 Quandong Street
Marrowbank VIC 3187
harbourlinedesignstudio.com.au
Nice to have
• Should have a calming feel to make me seem approachable but still professional.
Should not have
• No photos on the card or building plans.

```html
<!DOCTYPE html>
<html lang="en">
<head>
<meta charset="utf-8">
<title>Harbourline Design Studio – Business Card</title>
<link rel="stylesheet" href="https://fonts.googleapis.com/css2?family=Pacifico&family=Courgette&display=swap">
<style>
  :root {
    --backdrop: #ebe6de;
    --paper: #f4f4f3;
    --paper-shade: #e2e2e0;
    --brand-blue: #1ea8dc;
    --stripe-gap: #8fb9c8;
    --ink: #111111;
    --curve-shadow: rgba(0, 0, 0, 0.28);
  }
  * { box-sizing: border-box; margin: 0; padding: 0; }
  html, body {
    width: 1200px;
    height: 900px;
    overflow: hidden;
    background: var(--backdrop);
  }
  .canvas {
    position: relative;
    width: 1200px;
    height: 900px;
  }

  /* Front: vertical card */
  .card-front {
    position: absolute;
    left: 45px;
    top: 64px;
    width: 400px;
    height: 692px;
    background: var(--paper);
    box-shadow: 0 10px 22px rgba(0,0,0,0.25);
    overflow: hidden;
  }
  .card-front__top {
    position: absolute;
    left: 0; top: 0;
    width: 100%;
    height: 285px;
    background: radial-gradient(ellipse at 40% 30%, #fafafa 0%, var(--paper) 55%, var(--paper-shade) 100%);
  }
  .card-front__brand {
    position: absolute;
    top: 92px;
    width: 100%;
    text-align: center;
    font-family: "Pacifico", cursive;
    font-size: 38px;
    line-height: 56px;
    color: var(--brand-blue);
    white-space: nowrap;
  }
  .stripe-band {
    position: absolute;
    left: 0; top: 285px;
    width: 100%;
    height: 126px;
  }
  .card-front__details {
    position: absolute;
    left: 0; top: 346px;
    width: 100%;
    height: 317px;
    background: var(--paper);
    box-shadow: 0 -4px 8px rgba(0,0,0,0.12);
  }
  .person {
    position: absolute;
    right: 14px;
    top: 22px;
    text-align: right;
    font-family: "Pacifico", cursive;
    color: var(--ink);
    white-space: nowrap;
  }
  .person__name { font-size: 36px; line-height: 48px; }
  .person__title { font-family: "Courgette", cursive; font-size: 24px; line-height: 30px; }
  .contact {
    position: absolute;
    left: 14px;
    top: 141px;
    list-style: none;
    font-family: "Courgette", cursive;
    font-size: 16.5px;
    line-height: 30px;
    color: var(--ink);
    white-space: nowrap;
  }
  .contact__phone { font-size: 18px; }
  .card-front__foot {
    position: absolute;
    left: 0; bottom: 0;
    width: 100%;
    height: 29px;
    background: linear-gradient(180deg, var(--paper-shade), var(--paper));
  }

  /* Back: horizontal card */
  .card-back {
    position: absolute;
    left: 483px;
    top: 64px;
    width: 692px;
    height: 400px;
    background: var(--paper);
    box-shadow: 0 10px 22px rgba(0,0,0,0.25);
    overflow: hidden;
  }
  .card-back__brand {
    position: absolute;
    top: 118px;
    width: 100%;
    text-align: center;
    font-family: "Pacifico", cursive;
    font-size: 52px;
    line-height: 72px;
    color: var(--brand-blue);
    white-space: nowrap;
  }
  .card-back__wave {
    position: absolute;
    left: 0; top: 0;
    width: 692px;
    height: 400px;
  }
</style>
</head>
<body>
<main class="canvas">

  <section class="card-front" aria-label="Business card front">
    <div class="card-front__top"></div>
    <p class="card-front__brand">Harbourline Design<br>Studio</p>

    <svg class="stripe-band" viewBox="0 0 400 126" aria-hidden="true">
      <rect x="0" y="0" width="400" height="126" fill="var(--stripe-gap)"/>
      <g fill="var(--brand-blue)">
        <rect x="0" y="0" width="27" height="126"/>
        <rect x="44" y="0" width="25" height="126"/>
        <rect x="86" y="0" width="25" height="126"/>
        <rect x="128" y="0" width="25" height="126"/>
        <rect x="170" y="0" width="25" height="126"/>
        <rect x="212" y="0" width="25" height="126"/>
        <rect x="254" y="0" width="25" height="126"/>
        <rect x="296" y="0" width="25" height="126"/>
        <rect x="338" y="0" width="25" height="126"/>
        <rect x="380" y="0" width="20" height="126"/>
      </g>
    </svg>

    <div class="card-front__details">
      <div class="person">
        <p class="person__name">Rosalind Tebbutt</p>
        <p class="person__title">B.Arch</p>
      </div>
      <ul class="contact">
        <li class="contact__phone">0498 273 461</li>
        <li>rosalind@harbourlinedesignstudio.com.au</li>
        <li>rosalind@harbourlinedesignstudio.com.au</li>
        <li>14 Quandong Street Marrowbank VIC 3187</li>
      </ul>
    </div>
    <div class="card-front__foot"></div>
  </section>

  <section class="card-back" aria-label="Business card back">
    <p class="card-back__brand">Harbourline Design<br>Studio</p>
    <svg class="card-back__wave" viewBox="0 0 692 400" aria-hidden="true">
      <path d="M0,330 Q380,322 692,244" fill="none" stroke="var(--curve-shadow)" stroke-width="6"/>
      <path d="M0,336 Q380,328 692,250 L692,400 L0,400 Z" fill="var(--brand-blue)"/>
    </svg>
  </section>

</main>
</body>
</html>
```